Rise To Go Further! - Marketing, Training, Managment for Multifamily Professionals

Flyer for training event. I have to be able to edit location, times, speakers, cost,
We will have 2 to 4 speakers for each event. Each event may have a different topic relating to the main topic (Marketing, Training, Management). The idea is to get as many people to open or pick up the fly and say "I have to attend" this seminar. We are the experts in the industry and want to portray this with the flyer. Each speaker will have a topic and a certain amount of time. Each topic will be different.
Updates

Project Deadline Extended
Reason: I apologize for the new design deadline. I've been traveling extensively for work and unable to view submissions. Currently I am not traveling and able to dedicate time to view all of the wonderful submissions. I'm looking forward to selecting one. Thank you all for your understanding.

Target Market(s)

Multifamily - Apartment Communities, Owners, Apartment Associations, Leasing Agents, Marketing Directors, Managers, Presidents,

Industry/Entity Type

Marketing

Colors

Designer to choose colors to be used in the design.

Requirements
Must have
• Editable flyer. I have to be able to edit; location, times/date, speaker, cost, description.
• Sponsored by Tovali Power attached Logo for tovali
Nice to have
• Spot for photo of each speaker (2-4) speaker

```html
<!DOCTYPE html>
<html lang="en">
<head>
<meta charset="utf-8">
<title>Rise To Go Further! – Marketing Training Management</title>
<link rel="stylesheet" href="https://fonts.googleapis.com/css2?family=Bebas+Neue&family=Cinzel:wght@400;700&family=Roboto:wght@400;500;700&display=swap">
<style>
  :root {
    --magenta: #e6198a;
    --cyan: #1fa8d9;
    --yellow: #f7c51e;
    --ink: #141414;
    --charcoal: #3d3d3d;
    --paper: #ffffff;
    --backdrop: #ecebe8;
    --body: #2a2a2a;
  }
  * { box-sizing: border-box; margin: 0; padding: 0; }
  html, body { width: 1200px; height: 1200px; overflow: hidden; }
  body { background: var(--backdrop); font-family: "Roboto", sans-serif; }

  .flyer {
    position: absolute; left: 191px; top: 20px;
    width: 818px; height: 1160px;
    background: var(--paper); overflow: hidden;
    box-shadow: 0 6px 24px rgba(0,0,0,.18);
  }
  .hero-photo {
    position: absolute; left: 0; top: 0; width: 818px; height: 440px;
    background: linear-gradient(100deg, #2f3340 0%, #3b4a6e 35%, #5d79b8 60%, #9fb6de 85%, #c9d6ea 100%);
  }
  .hero-bands { position: absolute; left: 0; top: 400px; }

  .headline { position: absolute; left: 404px; top: 52px; font-family: "Bebas Neue", sans-serif; font-weight: 400; line-height: 1; }
  .headline span { display: block; font-size: 66px; letter-spacing: 0; }
  .headline .line-marketing { color: var(--magenta); padding-left: 6px; }
  .headline .line-training {
    color: var(--cyan); background: rgba(255,255,255,.85);
    width: 414px; height: 82px; padding: 8px 6px 0; margin-top: 10px;
  }
  .headline .line-management { color: var(--ink); padding-left: 6px; margin-top: 10px; }

  .sponsor { position: absolute; left: 60px; top: 572px; display: flex; align-items: center; gap: 12px; }
  .sponsor-name { font-family: "Roboto", sans-serif; font-weight: 700; font-size: 76px; color: var(--ink); line-height: 1; letter-spacing: -2px; }
  .sponsor-mark { width: 18px; height: 18px; background: var(--magenta); }

  .intro { position: absolute; left: 358px; top: 508px; width: 372px; }
  .intro h2 { font-family: "Cinzel", serif; font-weight: 400; font-size: 22px; color: var(--magenta); margin-bottom: 10px; }
  .intro p { font-size: 14.3px; line-height: 17.6px; color: var(--body); text-align: justify; }

  .info-bar { position: absolute; left: 0; top: 682px; width: 818px; height: 94px; }
  .info-left { position: absolute; left: 78px; top: 10px; color: var(--paper); }
  .info-left .venue { display: flex; gap: 10px; font-size: 15px; font-weight: 500; line-height: 19px; }
  .info-left .venue svg { margin-top: 6px; }
  .info-left .fee { margin-left: 34px; margin-top: 10px; font-size: 28px; font-weight: 700; color: var(--yellow); }
  .info-left .fee b { color: var(--paper); }
  .info-right { position: absolute; left: 450px; top: 6px; width: 330px; text-align: center; font-family: "Cinzel", serif; }
  .info-right .time { font-size: 44px; color: var(--paper); line-height: 1.1; }
  .info-right .date { font-size: 25px; color: var(--yellow); }
  .info-right .date sup { font-size: 12px; }

  .speakers { position: absolute; left: 34px; top: 790px; display: flex; gap: 31px; }
  .speaker { width: 162px; text-align: center; }
  .portrait-frame { position: relative; width: 162px; height: 168px; }
  .portrait-frame .tilt { position: absolute; left: 23px; top: 14px; width: 116px; height: 140px; }
  .tilt-a { background: var(--magenta); transform: rotate(-6deg); }
  .tilt-b { background: var(--yellow); transform: rotate(6deg); }
  .portrait {
    position: absolute; left: 22px; top: 10px; width: 118px; height: 146px;
    border: 3px solid var(--paper); border-radius: 4px;
  }
  .p1 { background: linear-gradient(#e9ebee, #c7cdd8 55%, #2f3e6e); }
  .p2 { background: linear-gradient(#6e94c8, #c9a08a 50%, #8c1e22); }
  .p3 { background: linear-gradient(#dfe6ee, #b99a82 50%, #e8e4e0); }
  .p4 { background: linear-gradient(#d6d9de, #caa590 50%, #2e3a5c); }
  .speaker-name {
    display: inline-block; margin-top: 8px; padding: 1px 10px;
    background: var(--cyan); color: var(--paper); border-radius: 6px;
    font-family: "Cinzel", serif; font-size: 15px;
  }
  .speaker-bio { margin-top: 8px; font-size: 10.6px; line-height: 13.8px; color: var(--body); text-align: justify; }

  .website { position: absolute; left: 0; width: 818px; top: 1098px; text-align: center; font-size: 14px; letter-spacing: 2px; color: var(--ink); }
  .footer-bands { position: absolute; left: 0; bottom: 0; }
</style>
</head>
<body>
  <main class="flyer">
    <div class="hero-photo" role="img" aria-label="Photo of a speaker at a podium with laptop addressing a seminar audience"></div>
    <svg class="hero-bands" width="818" height="120" viewBox="0 0 818 120">
      <polygon points="0,0 422,38 818,0 818,120 0,120" fill="#ffffff"/>
      <polygon points="0,0 422,38 818,0 818,10 422,48 0,10" fill="var(--yellow)"/>
      <polygon points="0,10 422,48 818,10 818,24 422,62 0,24" fill="var(--cyan)"/>
      <polygon points="0,24 250,42 0,110" fill="var(--cyan)"/>
    </svg>

    <h1 class="headline">
      <span class="line-marketing">Marketing</span>
      <span class="line-training">Training</span>
      <span class="line-management">Management</span>
    </h1>

    <div class="sponsor">
      <span class="sponsor-name">tovali</span>
      <span class="sponsor-mark"></span>
    </div>

    <section class="intro">
      <h2>Lorem Ipsum</h2>
      <p>Lorem Ipsum is simply dummy text of the printing and typesetting industry. Lorem Ipsum has been the industry's standard dummy text ever since the 1500s, when an unknown printer took a galley of type and scrambled it to make a type specimen book. It has survived not only five centuries, but also the leap into electronic typesetting, remaining essentially unchanged</p>
    </section>

    <section class="info-bar">
      <svg width="818" height="94" viewBox="0 0 818 94" style="position:absolute;left:0;top:0">
        <polygon points="0,0 402,0 384,94 0,94" fill="var(--charcoal)"/>
        <polygon points="414,0 818,0 818,94 396,94" fill="var(--charcoal)"/>
      </svg>
      <div class="info-left">
        <div class="venue">
          <svg width="22" height="22" viewBox="0 0 22 22"><path d="M11 2a6 6 0 0 0-6 6c0 4.5 6 11 6 11s6-6.5 6-11a6 6 0 0 0-6-6z" fill="none" stroke="var(--yellow)" stroke-width="2"/><circle cx="11" cy="8" r="2" fill="var(--yellow)"/></svg>
          <span>Lorem Ipsum is Simply<br>Dummy Text of The Printing</span>
        </div>
        <div class="fee"><b>$5</b> Entry Fee</div>
      </div>
      <div class="info-right">
        <div class="time">4PM to 8PM</div>
        <div class="date">25<sup>TH</sup>December,2017</div>
      </div>
    </section>

    <section class="speakers">
      <article class="speaker">
        <div class="portrait-frame"><div class="tilt tilt-a"></div><div class="tilt tilt-b"></div><div class="portrait p1" role="img" aria-label="Speaker portrait photo"></div></div>
        <span class="speaker-name">Lorem Ipsum</span>
        <p class="speaker-bio">Lorem Ipsum is simply dummy text of the printing and typesetting industry. Lorem Ipsum has been the industry's standard dummy text ever since the 1500s</p>
      </article>
      <article class="speaker">
        <div class="portrait-frame"><div class="tilt tilt-a"></div><div class="tilt tilt-b"></div><div class="portrait p2" role="img" aria-label="Speaker portrait photo"></div></div>
        <span class="speaker-name">Lorem Ipsum</span>
        <p class="speaker-bio">Lorem Ipsum is simply dummy text of the printing and typesetting industry. Lorem Ipsum has been the industry's standard dummy text ever since the 1500s</p>
      </article>
      <article class="speaker">
        <div class="portrait-frame"><div class="tilt tilt-a"></div><div class="tilt tilt-b"></div><div class="portrait p3" role="img" aria-label="Speaker portrait photo"></div></div>
        <span class="speaker-name">Lorem Ipsum</span>
        <p class="speaker-bio">Lorem Ipsum is simply dummy text of the printing and typesetting industry. Lorem Ipsum has been the industry's standard dummy text ever since the 1500s</p>
      </article>
      <article class="speaker">
        <div class="portrait-frame"><div class="tilt tilt-a"></div><div class="tilt tilt-b"></div><div class="portrait p4" role="img" aria-label="Speaker portrait photo"></div></div>
        <span class="speaker-name">Lorem Ipsum</span>
        <p class="speaker-bio">Lorem Ipsum is simply dummy text of the printing and typesetting industry. Lorem Ipsum has been the industry's standard dummy text ever since the 1500s</p>
      </article>
    </section>

    <div class="website">www.yourwebsite.com</div>

    <svg class="footer-bands" width="818" height="54" viewBox="0 0 818 54">
      <polygon points="0,10 818,20 818,34 0,30" fill="var(--magenta)"/>
      <polygon points="0,30 818,24 818,54 0,54" fill="var(--cyan)"/>
    </svg>
  </main>
</body>
</html>
```